Brasko Construction Business Card

I need a business card design for my company.
We are a construction/machinery company.
I would like to see my logo on the front of the card and my details on the other side
I would like the card to be black or dark grey in colour,with my logo as i send it or modified with a lighter blue colour
I would like to see the design kept fairly simple,but eye catching at the same time
Industry/Entity Type
Business
Contact Information for Business Card
Name
Phone Number
Address
Email
Colors
00a990
1b1b1b
000000
474747
ececec

```html
<!DOCTYPE html>
<html lang="en">
<head>
<meta charset="utf-8">
<title>Brasko Construction Business Card</title>
<link href="https://fonts.googleapis.com/css2?family=Open+Sans:wght@400;700&display=swap" rel="stylesheet">
<style>
  :root {
    --page: #d9d6d1;
    --card: #1b1b1b;
    --card-deep: #0e0e0e;
    --accent: #4cc6ea;
    --text: #ececec;
    --ghost: #474747;
  }
  * { margin: 0; padding: 0; box-sizing: border-box; }
  html, body { width: 1200px; height: 1023px; overflow: hidden; }
  body {
    background: var(--page);
    font-family: "Open Sans", Arial, sans-serif;
    display: flex;
    flex-direction: column;
    align-items: center;
    justify-content: center;
    gap: 70px;
  }
  .card {
    position: relative;
    width: 700px;
    height: 400px;
    border-radius: 6px;
    background: linear-gradient(135deg, #262626 0%, var(--card) 45%, var(--card-deep) 100%);
    box-shadow: 0 14px 30px rgba(0,0,0,0.35);
    overflow: hidden;
  }
  .card-front { display: flex; align-items: center; justify-content: center; }
  .brand-name {
    display: flex; align-items: center; gap: 16px;
    color: var(--accent);
    font-weight: 700;
    text-transform: uppercase;
    letter-spacing: 3px;
    line-height: 1.15;
  }
  .brand-dot { width: 22px; height: 22px; border-radius: 50%; background: var(--accent); flex: none; }
  .card-front .brand-name { font-size: 40px; }

  .card-back .contact {
    position: absolute; left: 48px; top: 56px; width: 290px;
  }
  .person-name { color: var(--accent); font-weight: 700; font-size: 20px; letter-spacing: 1px; text-transform: uppercase; }
  .person-role { color: var(--text); font-size: 14px; margin-top: 4px; }
  .rule { height: 1px; background: var(--accent); margin: 18px 0 20px; width: 260px; }
  .contact-list { list-style: none; }
  .contact-list li {
    display: flex; align-items: center; gap: 12px;
    color: var(--text); font-size: 14px; line-height: 1.35; margin-bottom: 10px;
  }
  .contact-list svg { width: 16px; height: 16px; flex: none; fill: var(--accent); }
  .card-back .brand-name {
    position: absolute; right: 44px; top: 62px; font-size: 28px;
  }
  .brand-lines { display: flex; flex-direction: column; }
  .machine-art {
    position: absolute; right: 80px; bottom: 0; width: 210px; height: 190px;
    background: linear-gradient(180deg, rgba(71,71,71,0.45), rgba(71,71,71,0.15));
    border-radius: 40px 40px 0 0;
  }
</style>
</head>
<body>
  <section class="card card-front">
    <div class="brand-name"><span class="brand-dot"></span>Brasko Construction</div>
  </section>

  <section class="card card-back">
    <div class="contact">
      <div class="person-name">Dr. Lena Varga</div>
      <div class="person-role">Site Manager</div>
      <div class="rule"></div>
      <ul class="contact-list">
        <li>
          <svg viewBox="0 0 16 16"><path d="M8 1a5 5 0 0 0-5 5c0 4 5 9 5 9s5-5 5-9a5 5 0 0 0-5-5zm0 7a2 2 0 1 1 0-4 2 2 0 0 1 0 4z"/></svg>
          <span>18 Quarry Lane, 40210<br>Millbrook, Northland</span>
        </li>
        <li>
          <svg viewBox="0 0 16 16"><rect x="1" y="1" width="14" height="14" rx="3"/></svg>
          <span>www.braskobuild.com</span>
        </li>
        <li>
          <svg viewBox="0 0 16 16"><path d="M4 1l3 3-2 2c1 2 3 4 5 5l2-2 3 3-2 3C7 15 1 9 1 3z"/></svg>
          <span>+1 555 0142 880</span>
        </li>
        <li>
          <svg viewBox="0 0 16 16"><path d="M3 2h10v12H3z"/></svg>
          <span>555 0199 310</span>
        </li>
        <li>
          <svg viewBox="0 0 16 16"><path d="M1 3h14v10H1zm1 1l6 5 6-5z"/></svg>
          <span>lena.varga@braskobuild.com</span>
        </li>
      </ul>
    </div>
    <div class="brand-name"><span class="brand-dot"></span><span class="brand-lines"><span>Brasko</span><span>Construction</span></span></div>
    <div class="machine-art" role="img" aria-label="Faint illustration of an excavator arm and bucket"></div>
  </section>
</body>
</html>
```